Basic / Quick Business Card

Quick easy design project!

Need a one sided basic business card that matches font & style of brand and bottle label for our gourmet condiment, Velvet Marlow Sauce. Velvet Marlow Sauce is sold in specialty retail, gourmet groceries and appears on chef-driven restaurant menus, so the target market is a high end, gourmet, artisan-made food-loving customer.

Files Included:
Sauce Bottle Label
Velvet Marlow Sauce Round Logos

**About the logos - the logo may be used in a circle or alone vertically as on side of the bottle label**

Layout of Card:
May be vertical or horizontal based on designer ideas.

Logo usage (in circle vs. stand alone vertical logo) is up to designers descretion as well.

Reverse side of business card will be various high end / professional product photos / food shots using us.prindex.com system. **Designer on this project will NOT design a reserve for the card.**

Paper that will be used for printing:
Prindex Basic - it's a WHITE paper, but we use a cream background on Velvet Marlow Sauce branding, so please take this into account on design to stay brand consistent.

Elements & Copy for Card:
1. Logo in either script horizontal or vertical version
2. Copy: "Artisan Made - Small Batch"
3. Name - Glen Worsley
4. Title - Creator
5. Phone - xxx.xxx.xxxx
6. xxxx@velvetmarlow.com
7. URL: velvetmarlowsauce.com
8. Social Media: @getvelvetmarlow on Chirpline / Friendwall / Snapgrid

Please provide final files in Illustrator or InDesign format.

```html
<!DOCTYPE html>
<html lang="en">
<head>
<meta charset="utf-8">
<title>Velvet Marlow Sauce – Business Card</title>
<link rel="stylesheet" href="https://fonts.googleapis.com/css2?family=Roboto+Slab:wght@400;500;700;800&family=Courier+Prime:wght@400&display=swap">
<style>
  :root {
    --ink: #0b0b0b;
    --cream: #f2f1e2;
    --gold: #f0a800;
    --backdrop: #e6e4dc;
    --charcoal: #2a2522;
  }
  * { margin: 0; padding: 0; box-sizing: border-box; }
  html, body {
    width: 1200px; height: 1019px; overflow: hidden;
    background: var(--backdrop);
  }
  .card {
    position: absolute; left: 75px; top: 209px;
    width: 1050px; height: 600px;
    background: var(--cream);
    overflow: hidden;
    box-shadow: 0 12px 30px rgba(0,0,0,0.18);
  }
  .card__band {
    position: absolute; left: 0; top: 0;
    width: 100%; height: 270px;
    background: var(--ink);
    border-bottom: 9px solid var(--gold);
  }
  .identity { position: absolute; left: 70px; top: 140px; }
  .identity__name {
    font-family: "Roboto Slab", serif; font-weight: 800;
    font-size: 42px; color: var(--gold); letter-spacing: 0.5px;
  }
  .identity__title {
    font-family: "Courier Prime", monospace;
    font-size: 32px; color: var(--cream); margin-top: 2px;
  }
  .contact {
    position: absolute; left: 70px; top: 330px;
    font-family: "Courier Prime", monospace;
    font-size: 28px; line-height: 42px; color: var(--ink);
  }
  .contact__label, .contact__networks {
    font-family: "Roboto Slab", serif; font-weight: 800; font-size: 26px;
  }
  .brand-seal {
    position: absolute; left: 640px; top: 95px;
    width: 350px; height: 350px;
  }
  .tagline {
    position: absolute; left: 700px; top: 470px;
    font-family: "Courier Prime", monospace;
    font-size: 34px; line-height: 42px; color: var(--gold);
  }
  .tagline span { display: block; }
  .tagline span + span { padding-left: 30px; }
</style>
</head>
<body>
  <div class="card">
    <div class="card__band"></div>

    <div class="identity">
      <div class="identity__name">Glen Worsley</div>
      <div class="identity__title">Creator</div>
    </div>

    <div class="contact">
      <div><span class="contact__label">Phone</span> 555.0148.2210</div>
      <div>glen@velvetmarlow.com</div>
      <div>velvetmarlowsauce.com</div>
      <div class="contact__networks">Chirpline / Friendwall / Snapgrid</div>
      <div>@getvelvetmarlow</div>
    </div>

    <svg class="brand-seal" viewBox="0 0 350 350" aria-label="Velvet Marlow Sauce">
      <circle cx="175" cy="175" r="165" fill="var(--cream)" stroke="var(--charcoal)" stroke-width="14"/>
      <text x="175" y="150" text-anchor="middle" font-family="Roboto Slab, serif" font-weight="700" font-size="46" fill="var(--charcoal)">Velvet</text>
      <text x="175" y="202" text-anchor="middle" font-family="Roboto Slab, serif" font-weight="700" font-size="46" fill="var(--charcoal)">Marlow</text>
      <text x="175" y="250" text-anchor="middle" font-family="Roboto Slab, serif" font-weight="700" font-size="30" fill="var(--charcoal)">Sauce</text>
    </svg>

    <div class="tagline">
      <span>Artisan Made</span>
      <span>Small Batch</span>
    </div>
  </div>
</body>
</html>
```